Natural Skin Care e commerce website

we are the distributor for natural skincare product , we would like to develop a e commerce website which encompass the ability to divide the product into face, body , baby , and base on ingredient , best seller, we are Verdal certified product the key point to focus is natural organic , no nasties, vegan , unpolluted , full of natural ingredient. manuka, olive nordic style temporary style website is preferred. the website name is Qelvora store.co , the web must have ability to take the order and let the brand upload their products

```html
<!DOCTYPE html>
<html lang="en">
<head>
<meta charset="utf-8">
<title>Qelvora Store – Natural Organic Skin Care</title>
<link href="https://fonts.googleapis.com/css2?family=Oswald:wght@400;500;600&family=Lato:wght@400;700&display=swap" rel="stylesheet">
<style>
:root{
  --green:#0e8a3e;
  --green-dark:#0b7534;
  --brown:#6e3a1d;
  --grey-bg:#eeeeee;
  --text:#555555;
  --star:#f4b400;
  --white:#ffffff;
}
*{margin:0;padding:0;box-sizing:border-box}
html,body{width:1200px;height:3338px;overflow:hidden;background:var(--white)}
body{position:relative;font-family:'Lato',sans-serif;color:var(--text)}
.abs{position:absolute}
.oswald{font-family:'Oswald',sans-serif}

/* top bar + header */
.topbar{left:0;top:0;width:1200px;height:29px;background:var(--green);color:var(--white);font-family:'Oswald',sans-serif;font-size:13px;letter-spacing:1px;text-align:center;line-height:29px}
.topbar-icons{right:165px;top:4px;display:flex;gap:16px}
.hero{left:0;top:29px;width:1200px;height:600px;overflow:hidden;
  background:
    radial-gradient(ellipse 260px 300px at 1000px 220px,#e8c2a6 0%,#d9a988 45%,rgba(217,169,136,0) 100%),
    radial-gradient(ellipse 170px 260px at 1140px 300px,#6b4330 0%,rgba(107,67,48,0) 100%),
    radial-gradient(ellipse 110px 240px at 640px 420px,#4a2a1c 0%,rgba(74,42,28,.6) 50%,rgba(74,42,28,0) 100%),
    radial-gradient(ellipse 70px 170px at 790px 460px,#2a5e3a 0%,rgba(42,94,58,0) 100%),
    radial-gradient(ellipse 60px 130px at 615px 500px,#8cbf4a 0%,rgba(140,191,74,0) 100%),
    linear-gradient(100deg,#e4f3ea 0%,#d8eee1 50%,#cde6d7 100%)}
.hero-visual{left:493px;top:29px;width:707px;height:600px}
.hero-leaf{left:0;top:402px;width:153px;height:227px;background:radial-gradient(ellipse at 20% 60%,#3d7a33,#245a22 60%,#1a4218);border-radius:0 90% 0 0}
.logo{left:162px;top:26px;text-align:center}
.logo-name{font-family:'Lato',sans-serif;font-size:28px;color:var(--brown);line-height:1}
.logo-sub{font-size:10px;letter-spacing:4px;color:var(--green);margin-top:4px;text-align:right}
.nav{right:161px;top:47px;display:flex;gap:31px;font-family:'Oswald',sans-serif;font-size:13px;letter-spacing:.8px;color:#333}
.nav .active{color:var(--brown)}
.hero-title{left:162px;top:210px;font-family:'Oswald',sans-serif;font-weight:500;font-size:52px;line-height:55px;color:var(--brown)}
.hero-text{left:162px;top:333px;width:360px;font-size:12px;line-height:20px;color:#333}
.btn{display:inline-block;background:var(--green);color:var(--white);font-family:'Oswald',sans-serif;font-size:13px;letter-spacing:1px;text-align:center}
.hero-btn{left:161px;top:393px;width:134px;height:44px;line-height:44px;font-size:14px}
.slider-dots{left:310px;top:564px;display:flex}
.slider-dots span{width:30px;height:20px}

/* categories */
.cat{top:631px;width:299px;height:298px;display:flex;align-items:flex-end;justify-content:center;padding-bottom:30px;color:var(--white);font-family:'Oswald',sans-serif;font-size:26px;letter-spacing:2px;text-shadow:0 1px 4px rgba(0,0,0,.35)}

/* best seller */
.section-title{left:0;width:1200px;text-align:center;font-family:'Oswald',sans-serif;font-weight:500;font-size:44px;color:var(--brown)}
.product{top:1089px;width:212px;text-align:center}
.product-img{width:150px;height:166px;margin:0 auto 36px;border-radius:6px}
.product-name{font-family:'Oswald',sans-serif;font-size:14px;color:var(--brown)}
.product-desc{font-size:10px;line-height:20px;margin-top:4px}
.stars{color:var(--star);font-size:13px;letter-spacing:1px;margin-top:4px}
.price{font-family:'Oswald',sans-serif;font-size:14px;color:#333;margin-top:3px}
.product .btn{width:113px;height:36px;line-height:36px;font-size:12px;margin-top:14px}

/* promos */
.promo{top:1501px;width:422px;height:224px}
.promo-left{left:161px;background:
  radial-gradient(ellipse 80px 100px at 300px 100px,#e8b56a 0%,#c99a55 50%,rgba(201,154,85,0) 100%),
  radial-gradient(ellipse 150px 80px at 330px 190px,#c88e4a 0%,rgba(200,142,74,0) 100%),
  linear-gradient(120deg,#2c4a57 0%,#3f6575 45%,#6b8a8e 70%,#a88a55 100%)}
.promo-right{left:616px;background:
  radial-gradient(ellipse 70px 130px at 240px 120px,#9ccf6f 0%,#7cbf4a 50%,rgba(124,191,74,0) 100%),
  radial-gradient(ellipse 70px 130px at 340px 120px,#5b7fd0 0%,#4a6cc2 45%,rgba(74,108,194,0) 100%),
  radial-gradient(ellipse 60px 100px at 410px 60px,#e78f6c 0%,rgba(231,143,108,0) 100%),
  linear-gradient(90deg,#f1f1ef 0%,#eceeea 50%,#dfe7da 100%)}
.promo-title{font-family:'Oswald',sans-serif;font-weight:500}

/* story */
.story-band{left:0;top:1801px;width:1200px;height:299px;background:
  radial-gradient(ellipse 400px 200px at 900px 80px,#9a5c32 0%,rgba(154,92,50,0) 100%),
  radial-gradient(ellipse 300px 160px at 200px 220px,#8c4f2a 0%,rgba(140,79,42,0) 100%),
  linear-gradient(110deg,#7a4322,#84492a 50%,#74401f)}
.story-grey{left:0;top:2100px;width:1200px;height:388px;background:var(--grey-bg)}
.story-card{left:161px;top:1969px;width:877px;height:298px;background:var(--white)}
.feature{top:2340px;width:180px;text-align:center;font-family:'Oswald',sans-serif;font-size:16px;color:var(--green)}
.feature svg{display:block;margin:0 auto 10px;height:48px}

/* testimonials */
.testi-text{left:300px;top:2769px;width:600px;text-align:center;font-size:11.5px;line-height:20px}

/* footer */
.footer{left:0;top:2994px;width:1200px;height:344px;background:var(--green);color:var(--white)}
.footer h4{font-family:'Oswald',sans-serif;font-weight:400;font-size:14px}
.foot-col{top:178px;font-size:11.5px;line-height:22px}
.social{display:flex;gap:8px;margin-top:14px}
.social span{width:28px;height:28px;border:1.5px solid var(--white);border-radius:50%}
</style>
</head>
<body>

<div class="abs topbar">FREE SAME DAY SHIPPING AND OFFER TODAY 50% DISCOUNT</div>
<div class="abs topbar-icons">
  <svg width="18" height="20" viewBox="0 0 18 20" fill="none" stroke="#fff" stroke-width="1.6"><circle cx="9" cy="6" r="4.5"/><path d="M1 19c1-5 4-7 8-7s7 2 8 7"/></svg>
  <svg width="22" height="20" viewBox="0 0 22 20" fill="none" stroke="#fff" stroke-width="1.6"><path d="M1 2h3l3 11h11l2-8H6"/><circle cx="9" cy="17" r="1.5"/><circle cx="17" cy="17" r="1.5"/></svg>
</div>

<section class="abs hero"></section>
<div class="abs hero-visual" role="img" aria-label="Skincare bottles and tubes beside a smiling woman touching her cheek"></div>
<div class="abs hero-leaf" role="img" aria-label="Large green monstera leaf"></div>

<div class="abs logo"><div class="logo-name">Qelvora</div><div class="logo-sub">STORE</div></div>
<nav class="abs nav"><span class="active">OUR STORY</span><span>SHOP</span><span>HOME</span><span>PRODUCTS</span><span>CONTACT</span></nav>

<h1 class="abs hero-title">Natural Organic for<br>you skin and body</h1>
<p class="abs hero-text">Lorem Ipsum is simply dummy text of the printing and typesetting industry. Lorem Ipsum has been the industry.</p>
<a class="abs btn hero-btn">SHOP NOW</a>
<div class="abs slider-dots"><span style="background:var(--brown)"></span><span style="background:var(--green)"></span></div>

<div class="abs cat" style="left:0;background:radial-gradient(ellipse 120px 150px at 150px 130px,#f0cdb4 0%,#e2b597 50%,rgba(226,181,151,0) 100%),radial-gradient(ellipse 120px 200px at 40px 120px,#7a4a30 0%,rgba(122,74,48,0) 100%),linear-gradient(135deg,#c99a7e,#dcb69c 60%,#cfa98f)" role="img" aria-label="Woman with glowing facial skin">FACE</div>
<div class="abs cat" style="left:300px;background:radial-gradient(ellipse 70px 150px at 150px 130px,#d7a77c 0%,rgba(215,167,124,0) 100%),radial-gradient(ellipse 200px 60px at 150px 270px,#f0ebe3 0%,rgba(240,235,227,0) 100%),linear-gradient(170deg,#c8a98b,#bd9a78 50%,#ddd1c2)" role="img" aria-label="Woman sunbathing on a lounger">BODY</div>
<div class="abs cat" style="left:601px;background:radial-gradient(ellipse 110px 110px at 150px 120px,#f3cfc3 0%,#e8b8ab 55%,rgba(232,184,171,0) 100%),radial-gradient(ellipse 200px 70px at 150px 270px,#f4e8e6 0%,rgba(244,232,230,0) 100%),linear-gradient(135deg,#d8a4a0,#cf9a96 50%,#ead2ce)" role="img" aria-label="Smiling baby lying on a blanket">BABY</div>
<div class="abs cat" style="left:901px;background:radial-gradient(ellipse 70px 90px at 250px 100px,#b7b64a 0%,#8c9a2e 55%,rgba(140,154,46,0) 100%),radial-gradient(ellipse 100px 80px at 110px 190px,#a9a63c 0%,#7a5a2a 40%,#5f6b22 70%,rgba(95,107,34,0) 100%),linear-gradient(135deg,#e6e3df,#d6d2cc 60%,#cfcac3)" role="img" aria-label="Halved avocado on marble">BASE ON INGREDIENT</div>

<h2 class="abs section-title" style="top:995px">BEST SELLER</h2>
<svg class="abs" style="left:124px;top:1180px" width="14" height="30" viewBox="0 0 14 30" fill="none" stroke="#666" stroke-width="1.3"><path d="M13 1L1 15l12 14"/></svg>
<svg class="abs" style="left:1062px;top:1180px" width="14" height="30" viewBox="0 0 14 30" fill="none" stroke="#666" stroke-width="1.3"><path d="M1 1l12 14L1 29"/></svg>

<div class="abs product" style="left:153px">
  <div class="product-img" role="img" aria-label="Green facial cleanser bottle with its box" style="background:radial-gradient(ellipse 30px 70px at 45px 100px,#2a5a38 0%,rgba(42,90,56,0) 100%),radial-gradient(ellipse 34px 75px at 108px 90px,#dfe8e0 0%,rgba(223,232,224,0) 100%)"></div>
  <div class="product-name">Product Name</div>
  <div class="product-desc">Lorem Ipsum is simply dummy text of the printing and typesetting industry.</div>
  <div class="stars">★★★★★</div><div class="price">$ 16.00</div><a class="btn">SHOP NOW</a>
</div>
<div class="abs product" style="left:381px">
  <div class="product-img" role="img" aria-label="Green herbal face pack tube" style="background:radial-gradient(ellipse 40px 80px at 75px 90px,#8cbf4a 0%,#6e9a3a 55%,rgba(110,154,58,0) 100%)"></div>
  <div class="product-name">Product Name</div>
  <div class="product-desc">Lorem Ipsum is simply dummy text of the printing and typesetting industry.</div>
  <div class="stars">★★★★★</div><div class="price">$ 16.00</div><a class="btn">SHOP NOW</a>
</div>
<div class="abs product" style="left:608px">
  <div class="product-img" role="img" aria-label="Amber hand wash pump bottle" style="background:radial-gradient(ellipse 34px 80px at 75px 95px,#6a3a2a 0%,#4a2a20 55%,rgba(74,42,32,0) 100%)"></div>
  <div class="product-name">Product Name</div>
  <div class="product-desc">Lorem Ipsum is simply dummy text of the printing and typesetting industry.</div>
  <div class="stars">★★★★★</div><div class="price">$ 16.00</div><a class="btn">SHOP NOW</a>
</div>
<div class="abs product" style="left:834px">
  <div class="product-img" role="img" aria-label="Dark serum spray bottle" style="background:radial-gradient(ellipse 30px 78px at 75px 95px,#3a342a 0%,#2a261f 55%,rgba(42,38,31,0) 100%)"></div>
  <div class="product-name">Product Name</div>
  <div class="product-desc">Lorem Ipsum is simply dummy text of the printing and typesetting industry.</div>
  <div class="stars">★★★★★</div><div class="price">$ 16.00</div><a class="btn">SHOP NOW</a>
</div>

<div class="abs promo promo-left" role="img" aria-label="Sunscreen tube on a beach"></div>
<div class="abs" style="left:188px;top:1522px;color:#fff">
  <div class="promo-title" style="font-size:33px;line-height:36px">NATURAL SUN<br>SKIN CARE</div>
  <div class="promo-title" style="font-size:40px;line-height:52px;color:#f5c400">35% <span style="color:#fff;font-size:32px">OFF</span></div>
  <a class="btn" style="width:114px;height:36px;line-height:36px;font-size:12px;margin-top:8px">SHOP NOW</a>
</div>
<div class="abs promo promo-right" role="img" aria-label="Facial spray bottles"></div>
<div class="abs" style="left:637px;top:1522px">
  <div class="promo-title" style="font-size:25px;color:var(--green);line-height:34px">Special summer</div>
  <div class="promo-title" style="font-size:29px;color:#222;line-height:38px">EVERY PRODUCT</div>
  <div class="promo-title" style="font-size:34px;color:#222;line-height:42px">15% <span style="font-size:27px">OFF</span></div>
  <a class="btn" style="background:var(--brown);width:114px;height:36px;line-height:36px;font-size:12px;margin-top:10px">SHOP NOW</a>
</div>

<div class="abs story-band" role="img" aria-label="Warm brown leaf texture"></div>
<div class="abs story-grey"></div>
<h2 class="abs section-title" style="top:1862px;color:#fff">OUR STORY</h2>
<p class="abs" style="left:400px;top:1919px;width:400px;text-align:center;color:#fff;font-size:10.5px;line-height:20px">Lorem Ipsum is simply dummy text of the printing and typesetting industry. Lorem Ipsum has been the industry's standard dummy text ever since the 1500s.</p>
<div class="abs story-card"></div>
<div class="abs" style="left:192px;top:2012px;width:384px;font-size:11.5px;line-height:20px">
  <p>Lorem Ipsum is simply dummy text of the printing and typesetting industry. Lorem Ipsum has been the industry's standard dummy text ever since the 1500s, when an unknown printer took a galley of type and scrambled it to make a type specimen book.</p>
  <p style="margin-top:18px">It has survived not only five centuries, but also the leap into electronic typesetting, remaining essentially unchanged.</p>
</div>
<svg class="abs" style="left:190px;top:2164px" width="232" height="62" viewBox="0 0 232 62">
  <circle cx="30" cy="30" r="28" fill="none" stroke="#2f7d3f" stroke-width="2.5"/><circle cx="30" cy="30" r="20" fill="none" stroke="#2f7d3f" stroke-width="1.2"/>
  <circle cx="112" cy="30" r="28" fill="none" stroke="#2f7d3f" stroke-width="2.5"/><circle cx="112" cy="30" r="20" fill="none" stroke="#2f7d3f" stroke-width="1.2"/>
  <circle cx="199" cy="30" r="28" fill="none" stroke="#7a3a25" stroke-width="2.5"/><circle cx="199" cy="30" r="20" fill="none" stroke="#7a3a25" stroke-width="1.2"/>
</svg>
<div class="abs" style="left:678px;top:2050px;text-align:left">
  <div style="font-size:78px;line-height:1;color:var(--brown)">Qelvora</div>
  <div style="font-size:28px;letter-spacing:9px;color:var(--green);text-align:right;margin-top:6px">STORE</div>
</div>

<div class="abs feature" style="left:167px">
  <svg width="54" height="40" viewBox="0 0 54 40" fill="none" stroke="var(--brown)" stroke-width="1.6"><path d="M6 36C14 24 26 18 48 14"/><path d="M20 26C14 14 22 4 34 4c0 12-6 20-14 22z"/><path d="M30 20c6-6 14-6 20-2-4 6-12 8-20 2z"/></svg>Herbal &amp; Natural</div>
<div class="abs feature" style="left:396px">
  <svg width="40" height="48" viewBox="0 0 40 48" fill="none" stroke="var(--brown)" stroke-width="1.6"><circle cx="20" cy="18" r="14"/><circle cx="20" cy="18" r="9"/><path d="M15 18l4 4 6-7"/><path d="M11 29l-4 14 6-3 3 6 4-12M29 29l4 14-6-3-3 6-4-12"/></svg>Certified</div>
<div class="abs feature" style="left:623px">
  <svg width="46" height="46" viewBox="0 0 46 46" fill="none" stroke="var(--brown)" stroke-width="1.6"><circle cx="23" cy="23" r="21"/><path d="M23 33c-8-5-11-9-11-13a5 5 0 0 1 11-2 5 5 0 0 1 11 2c0 4-3 8-11 13z"/></svg>Cruelty Free</div>
<div class="abs feature" style="left:850px">
  <svg width="48" height="48" viewBox="0 0 48 48" fill="none" stroke="var(--brown)" stroke-width="1.6"><path d="M10 26v-6a14 14 0 0 1 28 0v6"/><rect x="6" y="22" width="7" height="12" rx="3"/><rect x="35" y="22" width="7" height="12" rx="3"/><path d="M38 34c0 6-6 9-12 9"/><circle cx="24" cy="43" r="2.5"/></svg>Online Support</div>

<h2 class="abs section-title" style="top:2557px">TESTIMONIALS</h2>
<div class="abs" style="left:543px;top:2635px;width:114px;height:114px;border-radius:50%;background:radial-gradient(circle at 50% 45%,#e2b99b,#b07a55 60%,#8a5a3a)" role="img" aria-label="Client portrait"></div>
<div class="abs" style="left:543px;top:2636px;width:29px;height:29px;border-radius:50%;background:var(--green);color:#fff;font-family:Georgia,serif;font-size:24px;line-height:36px;text-align:center">“</div>
<p class="abs testi-text">Lorem Ipsum is simply dummy text of the printing and typesetting industry. Lorem Ipsum has been the industry's standard dummy text ever since the 1500s, when an unknown printer took a galley of type and scrambled it to make a type specimen book.</p>
<div class="abs" style="left:0;top:2844px;width:1200px;text-align:center;font-size:12px;font-weight:700;color:var(--green)">- CLIENT NAME</div>
<div class="abs stars" style="left:0;top:2864px;width:1200px;text-align:center;font-size:15px">★★★★★</div>
<svg class="abs" style="left:558px;top:2904px" width="84" height="14" viewBox="0 0 84 14"><circle cx="7" cy="7" r="6" fill="var(--brown)"/><circle cx="30" cy="7" r="5.5" fill="none" stroke="#777"/><circle cx="53" cy="7" r="5.5" fill="none" stroke="#777"/><circle cx="76" cy="7" r="5.5" fill="none" stroke="#777"/></svg>

<footer class="abs footer">
  <h3 class="abs oswald" style="left:162px;top:42px;font-weight:400;font-size:25px">NEWSLETTER</h3>
  <p class="abs" style="left:162px;top:80px;width:320px;font-size:11.5px;line-height:20px">Subscribe to stay with us and update our offers, discount, news and etc....</p>
  <div class="abs" style="left:507px;top:59px;width:348px;height:41px;border:1px solid #fff;font-size:11.5px;line-height:39px;padding-left:13px">Enter Email Here...</div>
  <div class="abs oswald" style="left:855px;top:59px;width:155px;height:41px;background:#fff;color:var(--green-dark);font-size:13px;letter-spacing:1px;line-height:41px;text-align:center">SUBSCRIBE</div>
  <div class="abs" style="left:162px;top:142px;width:876px;height:1px;background:rgba(255,255,255,.25)"></div>

  <div class="abs foot-col" style="left:162px;width:200px"><h4>Qelvora Store</h4><p style="margin-top:6px;line-height:20px">Lorem Ipsum is simply dummy text of the printing and typesetting industry. Lorem Ipsum has been the industry's standard dummy text ever since the 1500</p></div>
  <div class="abs foot-col" style="left:390px"><h4>Useful Links</h4><div style="margin-top:4px">Our Story<br>Shop<br>Home<br>Products<br>Contact</div></div>
  <div class="abs foot-col" style="left:617px;width:210px"><h4>Contact Info</h4>
    <div style="display:flex;gap:14px;margin-top:8px;line-height:17px;font-size:11px"><svg width="10" height="14" viewBox="0 0 10 14" fill="#fff" style="flex:none;margin-top:2px"><path d="M5 0a5 5 0 0 1 5 5c0 4-5 9-5 9S0 9 0 5a5 5 0 0 1 5-5z"/><circle cx="5" cy="5" r="2" fill="var(--green)"/></svg><span>Lorem Ipsum is simply dummy text of the printing.</span></div>
    <div style="display:flex;gap:14px;margin-top:10px;align-items:center;font-weight:700;font-size:12px"><svg width="12" height="12" viewBox="0 0 24 24" fill="#fff"><path d="M6.6 10.8a15 15 0 0 0 6.6 6.6l2.2-2.2c.3-.3.7-.4 1-.2 1.1.4 2.3.6 3.6.6.6 0 1 .4 1 1V20c0 .6-.4 1-1 1C10.6 21 3 13.4 3 4c0-.6.4-1 1-1h3.5c.6 0 1 .4 1 1 0 1.3.2 2.5.6 3.6.1.3 0 .7-.2 1z"/></svg>123 456 7890</div>
    <div style="display:flex;gap:14px;margin-top:8px;align-items:center;font-size:11px"><svg width="12" height="10" viewBox="0 0 12 10" fill="#fff"><path d="M0 0h12v10H0z"/><path d="M0 0l6 5 6-5" fill="none" stroke="var(--green)"/></svg>info@qelvorastore.com</div>
  </div>
  <div class="abs foot-col" style="left:845px;width:200px"><h4>Follow Us</h4>
    <div class="social" aria-label="Social links"><span></span><span></span><span></span><span></span><span></span></div>
    <p style="margin-top:10px;font-size:11px;line-height:20px">© Qelvorastore - 2020. All Rights Reserved.</p>
  </div>
</footer>

</body>
</html>
```